Catering company looking to promote business

We need a flyer design for our company named "Peel and Pulp." We cater/deliver açaí bowls and smoothies.

The objective of this flyer is to let companies know that we are taking açaí bowls and smoothie orders and they can be delivered to them.

Some key points we would like on the flyer:
- Photo of açaí bowl and smoothie
- Menu w/ pricing
- "No hidden delivery fees"
- 5 bowl or smoothie minimum
- Online ordering through website:
https://tillbox.example/shop/peelandpulp
- For the month of February --> Get one free topping and drizzle!
- FRIDAY DELIVERIES ONLY
- Questions? Call (555) 730-9182
- social media friendwall & snapreel @pnpulp
- website www.peelandpulp.example

font - hello beautiful

Target Market(s)

Juice, smoothies, açaí bowls

Industry/Entity Type

Business

Font styles to use
Other font styles liked:
• Hello Beautiful

Colors
a64599
b768aa
d3a5cc
eedced
f7f1f7
9bcb3c

Requirements
Must have
• Please match logo, fonts, color schemes, etc.

```html
<!DOCTYPE html>
<html lang="en">
<head>
<meta charset="UTF-8">
<title>Peel and Pulp – Açaí Bowl Flyer</title>
<link href="https://fonts.googleapis.com/css2?family=Caveat+Brush&family=Quicksand:wght@500;600;700&display=swap" rel="stylesheet">
<style>
  :root {
    --stage: #1d1c20;
    --plum: #5b3d97;
    --plum-deep: #4e3388;
    --magenta: #a64599;
    --orchid: #b768aa;
    --mauve: #d3a5cc;
    --blush: #eedced;
    --mist: #f7f1f7;
    --lilac: #c9badf;
    --pink-panel: #e3c6e0;
    --green: #7cb53a;
    --green-light: #9bcb3c;
    --white: #ffffff;
  }
  * { box-sizing: border-box; margin: 0; padding: 0; }
  html, body { width: 1200px; height: 848px; overflow: hidden; background: var(--stage); }
  .canvas { position: relative; width: 1200px; height: 848px; background: var(--stage); }

  .flyer {
    position: absolute; left: 272px; top: 0; width: 656px; height: 848px;
    background: linear-gradient(180deg, var(--mist) 0%, var(--white) 22%);
    overflow: hidden;
    font-family: "Quicksand", sans-serif;
  }
  .brush { font-family: "Caveat Brush", cursive; }

  .brand { position: absolute; left: 236px; top: 70px; display: flex; align-items: center; gap: 12px; }
  .brand-name { font-family: "Caveat Brush", cursive; font-size: 50px; color: var(--plum); line-height: 1; }
  .brand-dot { width: 18px; height: 18px; border-radius: 50%; background: var(--green-light); }

  .offer-title { position: absolute; left: 40px; top: 186px; font-size: 48px; color: var(--plum); line-height: 1; }
  .offer-price { position: absolute; left: 42px; top: 238px; font-size: 28px; color: var(--magenta); line-height: 1; }
  .offer-desc {
    position: absolute; left: 42px; top: 278px; width: 300px;
    font-weight: 700; font-size: 15px; line-height: 1.25; color: var(--magenta); text-transform: uppercase;
  }

  .photo-ring { position: absolute; left: 412px; top: 128px; width: 350px; height: 350px; }
  .photo {
    position: absolute; left: 436px; top: 152px; width: 302px; height: 302px; border-radius: 50%;
    background: radial-gradient(circle at 40% 40%, #f1ead8 0%, #e6d6b8 30%, #c94a55 62%, #5a6f86 100%);
  }

  .badge {
    position: absolute; width: 92px; height: 92px; border-radius: 50%; background: var(--orchid);
    color: var(--white); display: flex; align-items: center; justify-content: center; text-align: center;
    font-weight: 600; font-size: 12.5px; line-height: 1.15; padding: 10px;
  }
  .badge-fees { left: 350px; top: 168px; }
  .badge-min { left: 362px; top: 272px; }
  .badge-friday { left: 414px; top: 376px; font-weight: 700; text-transform: uppercase; }

  .extras-band {
    position: absolute; left: 18px; top: 474px; width: 620px; height: 48px; background: var(--green);
    display: flex; align-items: center; justify-content: flex-end; padding-right: 22px;
    color: var(--white); font-size: 30px;
  }

  .menu { position: absolute; left: 18px; top: 522px; width: 620px; height: 218px; display: flex; }
  .menu-col { position: relative; flex: 1; padding: 14px 16px; }
  .menu-fruits, .menu-drizzle { background: var(--pink-panel); }
  .menu-toppings { background: var(--lilac); }
  .menu-head { font-size: 30px; color: var(--plum); line-height: 1; margin-bottom: 8px; }
  .menu-head .cost { font-size: 22px; }
  .menu-list { list-style: none; color: var(--magenta); font-weight: 600; font-size: 14px; line-height: 1.3; }
  .menu-note {
    position: absolute; left: 0; right: 0; bottom: 0; height: 74px; background: var(--plum);
    color: var(--white); font-weight: 600; font-size: 12px; line-height: 1.3; padding: 12px 14px;
  }

  .contact-bar {
    position: absolute; left: 0; top: 740px; width: 656px; height: 58px; background: var(--plum-deep);
    display: flex; align-items: center; gap: 12px; padding-left: 28px; color: var(--white);
  }
  .contact-bar .ask { font-size: 30px; }
  .contact-bar .call { font-weight: 600; font-size: 30px; }

  .footer { position: absolute; left: 0; top: 798px; width: 656px; height: 50px; display: flex; }
  .footer-site {
    flex: 1; display: flex; align-items: center; padding-left: 40px;
    color: var(--plum); font-weight: 700; font-size: 22px; letter-spacing: 3px;
  }
  .footer-social {
    width: 190px; background: var(--orchid); border-left: 4px solid var(--white);
    display: flex; align-items: center; justify-content: center; gap: 10px; color: var(--white);
  }
  .social-dot { width: 22px; height: 22px; border-radius: 50%; background: var(--white); }
  .social-handle { font-family: "Caveat Brush", cursive; font-size: 26px; }
</style>
</head>
<body>
<div class="canvas">
  <article class="flyer">
    <div class="brand">
      <span class="brand-name">Peel and Pulp</span>
      <span class="brand-dot"></span>
    </div>

    <h1 class="offer-title brush">AÇAÍ BOWL</h1>
    <p class="offer-price brush">$9.00</p>
    <p class="offer-desc">Açaí sorbet topped with granola, bananas, strawberries, blueberries, coconut shavings and drizzled with honey</p>

    <svg class="photo-ring" viewBox="0 0 350 350" aria-hidden="true">
      <path d="M 40 90 A 165 165 0 0 1 330 60" fill="none" stroke="#5b3d97" stroke-width="6"/>
      <path d="M 60 300 A 165 165 0 0 0 300 320" fill="none" stroke="#a64599" stroke-width="4"/>
    </svg>
    <div class="photo" role="img" aria-label="Photo of an açaí bowl topped with sliced banana, blueberries, strawberries, coconut and seeds"></div>

    <div class="badge badge-fees">No hidden delivery fees</div>
    <div class="badge badge-min">5 bowl or smoothie minimum</div>
    <div class="badge badge-friday">Friday deliveries only</div>

    <div class="extras-band brush">WANT TO ADD SOMETHING EXTRA?</div>

    <section class="menu">
      <div class="menu-col menu-fruits">
        <h2 class="menu-head brush">FRUITS <span class="cost">$1.00</span></h2>
        <ul class="menu-list"><li>Bananas</li><li>Strawberries</li><li>Blueberries</li></ul>
        <p class="menu-note">Online ordering through website:<br>https://tillbox.example<br>/shop/peelandpulp</p>
      </div>
      <div class="menu-col menu-toppings">
        <h2 class="menu-head brush">TOPPINGS <span class="cost">.50¢</span></h2>
        <ul class="menu-list"><li>Almonds</li><li>Chia Seeds</li><li>Hemp Seeds</li><li>Cacao Nibs</li><li>Quinoa Puffs</li><li>Coconut Shavings</li><li>Granola</li></ul>
      </div>
      <div class="menu-col menu-drizzle">
        <h2 class="menu-head brush">DRIZZLE <span class="cost">.50¢</span></h2>
        <ul class="menu-list"><li>Peanut Butter</li><li>Almond Butter</li><li>Honey</li><li>Agave</li></ul>
        <p class="menu-note">For the month of February<br>Get one free topping<br>and drizzle!</p>
      </div>
    </section>

    <div class="contact-bar">
      <span class="ask brush">QUESTIONS?</span>
      <span class="call">Call (555) 730-9182</span>
    </div>

    <footer class="footer">
      <div class="footer-site">www.peelandpulp.example</div>
      <div class="footer-social">
        <span class="social-dot"></span>
        <span class="social-handle">@pnpulp</span>
      </div>
    </footer>
  </article>
</div>
</body>
</html>
```